Law Firm Needs Brochure Redesign Using New Logo

We are a personal injury law firm that does auto injuries and other personal injury cases. We want a new brochure that has our updated logo and information. Instead of gold and black, we want more navy, as matches the new logo. The Auto Liability portion should read: "(required by the state of Arizona in the amounts of $25,000 per person / $50,000 per accident, but a higher amount may be best )." The other information can remain the same. We'd like the brochure to keep the same professional tone as the previous brochure.
Our website is https://www.marbrenlegal.com/.

```html
<!DOCTYPE html>
<html lang="en">
<head>
<meta charset="utf-8">
<title>Marbren Legal – Car Accident Brochure</title>
<link href="https://fonts.googleapis.com/css2?family=Poppins:ital,wght@0,300;0,400;0,500;0,600;0,700;1,400&display=swap" rel="stylesheet">
<style>
:root{
  --navy:#0f213f;
  --navy-deep:#0a1426;
  --ink:#05080f;
  --gold:#c4a97e;
  --tan:#c2ab84;
  --paper:#f7f7f8;
  --mist:#e9eaec;
  --board:#a9a9a9;
  --white:#ffffff;
  --body:#33394a;
}
*{margin:0;padding:0;box-sizing:border-box}
html,body{width:1200px;height:1200px;overflow:hidden}
body{background:var(--board);font-family:'Poppins',sans-serif;position:relative}
.side-label{position:absolute;font-family:'Poppins',sans-serif;font-weight:400;font-size:42px;letter-spacing:12px;color:var(--navy);white-space:nowrap}
.side-label.outside{left:190px;top:336px;transform:translate(-50%,-50%) rotate(-90deg)}
.side-label.inside{left:958px;top:870px;transform:translate(-50%,-50%) rotate(90deg)}
.spread{position:absolute;overflow:hidden}
.spread.outer{left:233px;top:52px;width:679px;height:526px;background:var(--navy)}
.spread.inner{left:233px;top:610px;width:681px;height:527px;background:var(--paper)}
.spread>svg.shapes{position:absolute;inset:0;width:100%;height:100%}
.abs{position:absolute}
/* outside */
.stat-over{font-size:16px;font-weight:300;color:var(--white);line-height:1}
.stat-num{font-size:35px;font-weight:500;color:var(--gold);line-height:1}
.stat-note{font-size:7.4px;color:var(--white);line-height:1.25}
.pitch{left:28px;top:384px;width:192px;font-size:10.6px;line-height:13.7px;color:var(--white)}
.mail-panel{left:237px;top:14px;width:200px;height:496px;background:var(--white);border-radius:11px}
.return-address{left:256px;top:360px;height:140px;writing-mode:vertical-rl;transform:rotate(180deg);display:flex;gap:4px;align-items:flex-start}
.return-address .firm{font-size:13px;font-weight:700;color:var(--navy);display:flex;align-items:center;gap:4px;letter-spacing:.5px}
.mark-square{display:inline-block;width:9px;height:9px;background:var(--navy)}
.return-address .addr{font-size:7.6px;color:var(--navy);line-height:10px}
.brand{left:498px;top:26px;display:flex;align-items:center;gap:7px}
.brand .mark-square{width:16px;height:16px}
.brand .name{font-size:19px;font-weight:700;color:var(--navy);letter-spacing:1px}
.headline{left:474px;top:384px;font-size:19px;line-height:20px;color:var(--white);font-weight:300}
.headline strong{font-weight:600}
.tagline{left:474px;top:450px;font-size:8.6px;line-height:12px;color:var(--gold);font-style:italic}
.web{right:12px;top:496px;font-size:8.4px;letter-spacing:1.6px;color:var(--navy)}
/* inside */
.tips{left:13px;top:14px;width:202px;height:498px;background:var(--tan);border-radius:9px;overflow:hidden}
.tips-title{position:absolute;left:16px;top:14px;display:flex;align-items:center;gap:5px;color:var(--navy);border-bottom:1px solid var(--navy);width:175px;padding-bottom:4px}
.tips-top{font-weight:700;line-height:.9;text-align:center;padding-right:5px;border-right:1px solid var(--navy)}
.tips-top span{display:block;font-size:9px}
.tips-top b{display:block;font-size:22px}
.tips-head{font-size:14.2px;font-weight:600;line-height:17px}
.tips-list{position:absolute;left:13px;top:68px;width:182px;list-style:none}
.tips-list li{font-size:7.1px;line-height:8.3px;color:var(--body);padding-left:8px;position:relative;margin-bottom:7.2px}
.tips-list li::before{content:"";position:absolute;left:0;top:2.5px;border-left:3px solid var(--navy);border-top:2px solid transparent;border-bottom:2px solid transparent}
.tips-list b{color:var(--navy-deep);font-weight:600}
.photo{position:absolute}
.banner{position:absolute;height:24px;background:var(--tan);color:var(--white);font-weight:600;display:flex;align-items:center;padding-left:11px;clip-path:polygon(0 0,100% 0,calc(100% - 22px) 100%,0 100%)}
.copy{position:absolute;font-size:8.2px;line-height:10.2px;color:var(--body)}
.copy strong{color:var(--navy);font-weight:600}
.coverage{left:247px;top:272px;width:205px}
.coverage h4{font-size:8px;font-weight:600;color:var(--navy);margin:7px 0 5px;padding-left:10px;position:relative}
.coverage h4::before{content:"";position:absolute;left:0;top:3px;border-left:3px solid var(--navy);border-top:2px solid transparent;border-bottom:2px solid transparent}
.contact{right:16px;top:428px;text-align:right;color:var(--white);font-size:11.2px;line-height:13px}
.contact .firm{color:var(--gold);font-weight:600;font-size:13.5px;margin-bottom:3px}
</style>
</head>
<body>

<div class="side-label outside">OUTSIDE</div>
<div class="side-label inside">INTSIDE</div>

<!-- Outside spread -->
<section class="spread outer">
  <svg class="shapes" viewBox="0 0 849 657" preserveAspectRatio="none">
    <defs>
      <linearGradient id="handsTone" x1="0" y1="0" x2="0" y2="1">
        <stop offset="0" stop-color="#2a3f63"/><stop offset=".6" stop-color="#0c1628"/><stop offset="1" stop-color="#05080f"/>
      </linearGradient>
      <linearGradient id="driveTone" x1="0" y1="0" x2="1" y2="1">
        <stop offset="0" stop-color="#2b2f3c"/><stop offset=".45" stop-color="#5c4a5a"/><stop offset="1" stop-color="#d9a9b5"/>
      </linearGradient>
    </defs>
    <rect x="0" y="0" width="296" height="657" fill="var(--ink)"/>
    <polygon points="0,0 70,0 296,155 296,240 0,260" fill="url(#handsTone)" role="img" aria-label="Photo: open hands sheltering a glowing car icon"/>
    <line x1="70" y1="0" x2="296" y2="155" stroke="#fff" stroke-width="4"/>
    <polygon points="0,468 138,398 296,500 296,657 0,657" fill="var(--navy)"/>
    <polyline points="0,462 138,395 296,496" fill="none" stroke="#fff" stroke-width="4"/>
    <polygon points="546,0 849,0 849,275 640,410 546,345" fill="url(#driveTone)" role="img" aria-label="Photo: driver's hand with wristwatch on a steering wheel at dusk"/>
    <polygon points="546,345 640,410 546,490" fill="var(--mist)"/>
    <polygon points="665,418 849,290 849,305 690,418" fill="var(--gold)"/>
    <polygon points="700,657 849,555 849,657" fill="var(--mist)"/>
    <polygon points="645,613 849,613 849,637 625,637" fill="var(--gold)"/>
    <polygon points="310,657 340,637 360,637 330,657" fill="#fff"/>
  </svg>

  <div class="abs stat-over" style="left:28px;top:170px">over</div>
  <div class="abs stat-num" style="left:28px;top:184px">107,000</div>
  <div class="abs stat-note" style="left:30px;top:221px;width:140px">crashes will happen in the state of Arizona this year.</div>
  <div class="abs stat-over" style="left:28px;top:256px">over</div>
  <div class="abs stat-num" style="left:28px;top:268px">700</div>
  <div class="abs stat-note" style="left:94px;top:274px;width:80px">of them will result in fatalities.</div>
  <p class="abs pitch">If we don't win, you don't pay attorney fees. That seems fair to us. Know what's happening with your case, get the answers to your questions and work on getting better with the confidence that you've got an excellent group of people working for you.</p>

  <div class="abs mail-panel"></div>
  <div class="abs return-address">
    <div class="firm"><span class="mark-square"></span>MARBREN LEGAL</div>
    <div class="addr">4870 N. Cedar Ridge Drive Suite B114<br>Phoenix AZ 85016</div>
  </div>

  <div class="abs brand"><span class="mark-square"></span><span class="name">MARBREN LEGAL</span></div>
  <h1 class="abs headline">PROTECT YOUR<br>FAMILY IN CASE OF<br><strong>A CAR ACCIDENT</strong></h1>
  <p class="abs tagline">A little knowledge and preparation<br>go a long way</p>
  <div class="abs web">WWW.MARBRENLEGAL.COM</div>
</section>

<!-- Inside spread -->
<section class="spread inner">
  <svg class="shapes" viewBox="0 0 851 659" preserveAspectRatio="none">
    <defs>
      <linearGradient id="beltTone" x1="0" y1="0" x2="1" y2="1">
        <stop offset="0" stop-color="#d9c3ae"/><stop offset=".5" stop-color="#3a3d44"/><stop offset="1" stop-color="#1f5b5a"/>
      </linearGradient>
      <linearGradient id="wreckTone" x1="0" y1="0" x2="1" y2="1">
        <stop offset="0" stop-color="#6f7f7a"/><stop offset=".5" stop-color="#3b3f46"/><stop offset="1" stop-color="#9aa0a8"/>
      </linearGradient>
      <linearGradient id="crashTone" x1="0" y1="0" x2="1" y2="0">
        <stop offset="0" stop-color="#1d2230"/><stop offset=".6" stop-color="#6c7078"/><stop offset="1" stop-color="#b9bcc1"/>
      </linearGradient>
    </defs>
    <polygon points="0,0 700,0 270,290 270,659 0,659" fill="var(--navy)"/>
    <polygon points="268,275 330,235 340,235 268,290" fill="var(--gold)"/>
    <polygon points="570,372 851,218 851,405 570,590" fill="url(#wreckTone)" role="img" aria-label="Photo: distressed driver leaning out of a damaged car after a collision"/>
    <polygon points="570,372 600,372 570,392" fill="var(--navy)"/>
    <polygon points="500,659 851,405 851,659" fill="var(--navy)"/>
    <polygon points="735,525 851,445 851,462 760,525" fill="var(--gold)"/>
    <rect x="304" y="22" width="248" height="240" rx="12" fill="url(#beltTone)" role="img" aria-label="Photo: hands fastening a seatbelt buckle"/>
  </svg>

  <div class="abs tips">
    <div class="tips-title">
      <div class="tips-top"><span>TOP</span><b>10</b></div>
      <div class="tips-head">Tips to<br>Avoid a Crash</div>
    </div>
    <ul class="tips-list">
      <li><b>Anyone making a left turn must wait for all oncoming traffic to clear before proceeding.</b> Yes, even if the light has turned yellow. Wait to be sure that all traffic has stopped.</li>
      <li><b>When your light turns green,</b> check to be sure that no vehicles are entering the intersection late.</li>
      <li><b>Allow plenty of room between you and the car in front of you.</b> Traffic can stop in an instant, even if you can't see anything ahead.</li>
      <li><b>Avoid being distracted.</b> Teenagers are especially susceptible to losing focus if there are too many friends in the car.</li>
      <li><b>Keep the volume of your radio down and never wear headphones.</b> Cars are very soundproof these days, but you need to be able to hear an ambulance or police siren.</li>
      <li><b>Be especially careful on the weekends and early morning hours.</b></li>
      <li><b>Don't speed.</b> Speed is a factor in most crashes. Street lights are timed and the freeway has traffic. It's likely you won't get there much faster even if you do speed.</li>
      <li><b>Don't drink and drive.</b> Many cab companies offer a free service to get you home safe.</li>
      <li><b>Use your turn signals.</b> This gives an early warning to vehicles you may not be able to see.</li>
    </ul>
    <svg class="photo" style="left:0;top:385px;width:202px;height:113px" viewBox="0 0 202 113" preserveAspectRatio="none">
      <rect width="202" height="113" fill="url(#crashTone)" role="img" aria-label="Photo: two cars crumpled in a front-end collision"/>
    </svg>
  </div>

  <div class="banner" style="left:470px;top:22px;width:180px;font-size:13.4px">Model Safe Behavior</div>
  <p class="copy" style="left:472px;top:62px;width:205px">Always buckle up. Always put your children in car seats/boosters that are rated for their height and weight.</p>

  <div class="banner" style="left:470px;top:113px;width:202px;font-size:13.4px">Never Text While Driving</div>
  <p class="copy" style="left:472px;top:148px;width:205px">Studies have shown that texting while driving is as dangerous as driving intoxicated.</p>
  <p class="copy" style="left:471px;top:174px;width:180px"><strong>Show your children that no text is more important than your safety.<br>It can wait.</strong></p>

  <div class="banner" style="left:246px;top:234px;width:238px;font-size:14.6px">Have the Right Coverage</div>
  <div class="copy coverage">
    <p>Many people don't know about the different kinds of insurance available. In addition to health insurance, we suggest:</p>
    <h4>Auto Liability</h4>
    <p>(required by the state of Arizona in the amounts of $25,000 per person / $50,000 per accident, but a higher amount may be best ).</p>
    <h4>Uninsured or Underinsured Motorist Coverage.</h4>
    <p>This protects YOU when the other driver doesn't have insurance or not enough.</p>
    <h4>Medical Payments Coverage.</h4>
    <p>Up to $5,000 in coverage will be paid out to you no matter who is at fault in an accident and does not need to be reimbursed.</p>
    <h4>Homeowners / Renters Insurance.</h4>
    <p>Protects you in case of injuries on your property as well as damage to your home from covered events</p>
  </div>

  <address class="abs contact" style="font-style:normal">
    <div class="firm">Marbren Legal Group</div>
    4870 N. Cedar Ridge Drive<br>
    Suite B114 Phoenix AZ 85016<br>
    602.555.0148<br>
    info@MarbrenLegal.com<br>
    MarbrenLegal.com
  </address>
</section>

</body>
</html>
```